Business Card Design

We are starting up a new Family run Business mainly offering a Free House Clearance service. We also offer the following chargeable services which include a Removals Service, Delivery and Collection of Items sold or purchased on Bidloft, Swapwren etc, including Motorcycles, Piano's, Furniture, Electrical appliances.
As there are a few Companies offering similar services we need to stand out and show what we do at a glance while appearing Professional and approachable
Updates

TidyNests

i  am liking some of the colours and designs so far but would like to see a few of our services listed as 1 or 2 have already done if this is possible and maybe some emphasis on the FREE House Clearance. thank you 
best regards
derek

Target Market(s)

Commercial and Domestic Tenants and Landlords aswell as Families looking for a friendly sympathetic clearance service after bereavement

Industry/Entity Type

Business

Contact Information for Business Card

TidyNests,
HouseClearance and Removals,
Marlow Dene
LM47 2QT
Tel: 07815239604
Email: enquiries@tidynests-example.info

```html
<!DOCTYPE html>
<html lang="en">
<head>
<meta charset="utf-8">
<title>TidyNests Business Card</title>
<link href="https://fonts.googleapis.com/css2?family=Montserrat:wght@300;400;600&display=swap" rel="stylesheet">
<style>
  :root {
    --backdrop: #c3c3c3;
    --brand-blue: #02adee;
    --band-line: #0490c6;
    --handle-dark: #024a62;
    --handle-grey: #6a6b6a;
    --divider-grey: #c9c9c9;
    --white: #ffffff;
  }
  html, body {
    margin: 0;
    padding: 0;
    width: 1200px;
    height: 1000px;
    overflow: hidden;
    background: var(--backdrop);
    font-family: "Montserrat", sans-serif;
  }
  .card {
    position: absolute;
    left: 257px;
    width: 685px;
    height: 451px;
    overflow: hidden;
  }
  .card--front { top: 26px; background: var(--brand-blue); color: var(--white); }
  .card--back { top: 518px; background: var(--white); color: var(--brand-blue); }
  .card__banner {
    position: absolute;
    left: 0; top: 0;
    width: 100%;
    height: 74px;
    display: flex;
    align-items: center;
    justify-content: center;
    font-size: 25px;
    font-weight: 400;
    letter-spacing: 0.5px;
    box-sizing: border-box;
    padding-top: 6px;
  }
  .card__rule {
    position: absolute;
    left: 0; top: 73px;
    width: 100%;
    height: 5px;
  }
  .card--front .card__rule { background: var(--band-line); }
  .card--back .card__rule { background: var(--divider-grey); }
  .card__handle {
    position: absolute;
    left: 233px; top: 96px;
    width: 219px;
    height: 48px;
    border-radius: 24px;
  }
  .card--front .card__handle { background: var(--handle-dark); }
  .card--back .card__handle { background: var(--handle-grey); }
  .card__arrow {
    position: absolute;
    top: 102px;
    width: 60px;
    height: 236px;
  }
  .card__arrow--left { left: 31px; }
  .card__arrow--right { left: 594px; }
  .brand {
    position: absolute;
    left: 0; top: 196px;
    width: 100%;
    text-align: center;
  }
  .brand__name {
    margin: 0;
    font-size: 66px;
    font-weight: 600;
    line-height: 1;
    letter-spacing: 0.5px;
  }
  .brand__tagline {
    margin: 4px 0 0;
    font-size: 22px;
    font-weight: 300;
  }
  .contact {
    position: absolute;
    left: 0; top: 208px;
    width: 100%;
    text-align: center;
    font-style: normal;
  }
  .contact__town {
    display: block;
    font-size: 56px;
    font-weight: 400;
    line-height: 1.05;
  }
  .contact__line {
    display: block;
    font-size: 25px;
    font-weight: 400;
    line-height: 33px;
  }
</style>
</head>
<body>
  <section class="card card--front">
    <div class="card__banner">FREE HOUSE CLEARANCE</div>
    <div class="card__rule"></div>
    <div class="card__handle"></div>
    <svg class="card__arrow card__arrow--left" viewBox="0 0 60 236" aria-hidden="true">
      <polygon points="30,0 60,70 0,70" fill="#ffffff"/>
      <rect x="27" y="68" width="6" height="168" fill="#ffffff"/>
    </svg>
    <svg class="card__arrow card__arrow--right" viewBox="0 0 60 236" aria-hidden="true">
      <polygon points="30,0 60,70 0,70" fill="#ffffff"/>
      <rect x="27" y="68" width="6" height="168" fill="#ffffff"/>
    </svg>
    <div class="brand">
      <h1 class="brand__name">TidyNests</h1>
      <p class="brand__tagline">HouseClearance and Removals</p>
    </div>
  </section>

  <section class="card card--back">
    <div class="card__banner">FREE HOUSE CLEARANCE</div>
    <div class="card__rule"></div>
    <div class="card__handle"></div>
    <svg class="card__arrow card__arrow--left" viewBox="0 0 60 236" aria-hidden="true">
      <polygon points="30,0 60,70 0,70" fill="#02adee"/>
      <rect x="27" y="68" width="6" height="168" fill="#02adee"/>
    </svg>
    <svg class="card__arrow card__arrow--right" viewBox="0 0 60 236" aria-hidden="true">
      <polygon points="30,0 60,70 0,70" fill="#02adee"/>
      <rect x="27" y="68" width="6" height="168" fill="#02adee"/>
    </svg>
    <address class="contact">
      <span class="contact__town">Marlow Dene</span>
      <span class="contact__line">LM47 2QT</span>
      <span class="contact__line">Tel: 07815239604</span>
      <span class="contact__line">Email: enquiries@tidynests-example.info</span>
    </address>
  </section>
</body>
</html>
```